Quill Ridge Business cards

We need business cards for our aviation company called Quill Ridge Aviation. The colour scheme is the same as the one in the logo you design (metallic green/ similar to the colours on the aircraft). The design needs to be unique and stand out.

Industry/Entity Type

Business

```html
<!DOCTYPE html>
<html lang="en">
<head>
<meta charset="utf-8">
<title>Quill Ridge Aviation – Business Cards</title>
<link href="https://fonts.googleapis.com/css2?family=Smooch+Sans:wght@300;400&family=Questrial&display=swap" rel="stylesheet">
<style>
  :root {
    --green: #59b245;
    --green-deep: #428a34;
    --card: #e5e5e5;
    --ink: #333333;
    --page: #ffffff;
  }
  html, body {
    margin: 0;
    padding: 0;
    overflow: hidden;
    background: var(--page);
  }
  .canvas {
    position: relative;
    width: 1200px;
    height: 921px;
    overflow: hidden;
    background: var(--page);
  }
  .brand-mark {
    position: absolute;
    left: 0;
    top: 195px;
    width: 336px;
    text-align: center;
    font-family: "Smooch Sans", sans-serif;
    font-weight: 400;
    font-size: 80px;
    line-height: 1;
    color: var(--green);
    letter-spacing: 1px;
  }
  .card {
    position: absolute;
    left: 400px;
    width: 763px;
    background: var(--card);
    overflow: hidden;
  }
  .card--front { top: 45px; height: 435px; }
  .card--back { top: 493px; height: 420px; }
  .tag-hole {
    position: absolute;
    left: 38px;
    width: 64px;
    height: 64px;
  }
  .card--front .tag-hole { top: 185px; }
  .card--back .tag-hole { top: 186px; }
  .front-name {
    position: absolute;
    left: 140px;
    right: 30px;
    top: 140px;
    font-family: "Smooch Sans", sans-serif;
    font-weight: 300;
    font-size: 160px;
    line-height: 1;
    color: var(--green);
    letter-spacing: 2px;
    text-align: center;
    white-space: nowrap;
  }
  .company-name {
    position: absolute;
    right: 20px;
    top: 24px;
    margin: 0;
    font-family: "Smooch Sans", sans-serif;
    font-weight: 400;
    font-size: 86px;
    line-height: 1;
    color: var(--green);
    letter-spacing: 1px;
    white-space: nowrap;
  }
  .contact {
    position: absolute;
    right: 48px;
    top: 110px;
    margin: 0;
    padding: 0;
    list-style: none;
    font-family: "Questrial", sans-serif;
    font-size: 24px;
    color: var(--ink);
    text-align: right;
  }
  .contact li {
    height: 48px;
    line-height: 48px;
    white-space: nowrap;
  }
  .contact .label { letter-spacing: 1px; margin-right: 8px; }
  .contact .fill { font-size: 16px; letter-spacing: 0.5px; }
</style>
</head>
<body>
<main class="canvas">
  <div class="brand-mark">Quill Ridge</div>

  <section class="card card--front">
    <svg class="tag-hole" viewBox="0 0 64 64" aria-hidden="true">
      <circle cx="32" cy="32" r="27" fill="var(--page)" stroke="var(--green)" stroke-width="8"/>
    </svg>
    <div class="front-name">QUILL RIDGE</div>
  </section>

  <section class="card card--back">
    <svg class="tag-hole" viewBox="0 0 64 64" aria-hidden="true">
      <circle cx="32" cy="32" r="27" fill="var(--page)" stroke="var(--green)" stroke-width="8"/>
    </svg>
    <h1 class="company-name">QUILL RIDGE AVIATION</h1>
    <ul class="contact">
      <li><span class="label">Tel:</span><span class="fill">...............................</span></li>
      <li><span class="label">E:</span><span class="fill">...................................</span>@<span class="fill">.........................</span></li>
      <li><span class="label">A:</span><span class="fill">..............................................</span></li>
      <li><span class="fill">.................................................</span></li>
      <li><span class="fill">.......................................................</span></li>
    </ul>
  </section>
</main>
</body>
</html>
```